Business Card Design

I am a voice actor and need a business card to match the design of my website, www.tamsinharlowe.com. The colors are red, black and white. I've attached a pic of the back of a business card I thought was cool that for my design, could maybe have the black and white background from my website and the website address going across the middle of the card in red...or within a red square and white lettering..?? Just play around with it. Also wanting to keep the fonts on the business card similar to those on the website. I also attached a copy of the front of a business card that I liked. My design does not have to look like this.
I have a tag line, but not sure it will be too much to add to my business card or not. Would like to see the design with the tag and without it. "Voiced with Heart..." you'll see it on my website.
I will be ordering additional items from the chosen designer. I need a nice logo to use on my invoices, notecards and I need a letterhead design. Thank you so much for being artistically brilliant!
Industry/Entity Type
Business
Contact Information for Business Card
Tamsin Harlowe
Voice Actor
Email: Tamsin@TamsinHarlowe.com
Website: www.TamsinHarlowe.com

```html
<!DOCTYPE html>
<html lang="en">
<head>
<meta charset="utf-8">
<title>Tamsin Harlowe – Business Card</title>
<link rel="stylesheet" href="https://fonts.googleapis.com/css2?family=Libre+Baskerville:wght@400;700&family=Mrs+Saint+Delafield&display=swap">
<style>
  :root {
    --canvas: #ffffff;
    --ink: #111111;
    --wine-deep: #1a0406;
    --wine: #5a0e14;
    --wine-glow: #7a1a20;
    --silver-light: #ffffff;
    --silver-mid: #d9d9dc;
    --silver-dark: #9a9aa0;
    --panel-light: #f2f2f2;
    --panel-dark: #1b1b1b;
  }
  * { margin: 0; padding: 0; box-sizing: border-box; }
  html, body {
    width: 1200px; height: 1000px; overflow: hidden;
    background: var(--canvas);
  }
  .canvas { position: relative; width: 1200px; height: 1000px; }

  /* Front */
  .card-front {
    position: absolute; left: 200px; top: 30px;
    width: 782px; height: 447px; border-radius: 8px; overflow: hidden;
  }
  .card-front__pattern {
    position: absolute; inset: 0;
    background: radial-gradient(ellipse at 50% 35%, var(--wine-glow) 0%, var(--wine) 40%, var(--wine-deep) 100%);
  }
  .card-front__name {
    position: absolute; left: 0; right: 0; top: 196px;
    text-align: center; line-height: 1.2;
    font-family: "Libre Baskerville", serif; font-weight: 400; font-size: 72px;
    background: linear-gradient(180deg, var(--silver-light) 10%, var(--silver-mid) 55%, var(--silver-dark) 100%);
    -webkit-background-clip: text; background-clip: text; color: transparent;
    filter: drop-shadow(3px 4px 3px rgba(0,0,0,0.85));
  }

  /* Back */
  .card-back {
    position: absolute; left: 200px; top: 527px;
    width: 777px; height: 441px;
    border: 4px solid var(--ink); border-radius: 10px; overflow: hidden;
    background: var(--canvas);
  }
  .card-back__art {
    position: absolute; left: 0; top: 0; width: 188px; height: 100%;
    background: linear-gradient(175deg, var(--panel-light) 0%, var(--panel-light) 45%, #6a6a6a 75%, var(--panel-dark) 100%);
    border-right: 4px solid var(--ink);
  }
  .card-back__name {
    position: absolute; left: 233px; top: 80px;
    font-family: "Libre Baskerville", serif; font-weight: 700;
    font-size: 42px; color: var(--ink); white-space: nowrap;
  }
  .card-back__role {
    position: absolute; left: 500px; top: 130px;
    font-family: "Mrs Saint Delafield", cursive; font-size: 54px;
    color: var(--ink); white-space: nowrap;
  }
  .contact {
    position: absolute; left: 233px;
    display: flex; align-items: center; gap: 12px;
    font-family: "Libre Baskerville", serif; font-size: 28px; color: var(--ink);
    white-space: nowrap;
  }
  .contact--email { top: 252px; }
  .contact--web { top: 334px; left: 240px; gap: 16px; }
  .contact__icon { flex: none; }
</style>
</head>
<body>
<main class="canvas">
  <section class="card-front">
    <div class="card-front__pattern" role="img" aria-label="Dark red ornamental damask pattern background"></div>
    <h1 class="card-front__name">Tamsin Harlowe</h1>
  </section>

  <section class="card-back">
    <div class="card-back__art" role="img" aria-label="Black and white voice artwork panel"></div>
    <h2 class="card-back__name">Tamsin Harlowe</h2>
    <p class="card-back__role">Voice Actor</p>

    <p class="contact contact--email">
      <svg class="contact__icon" width="40" height="28" viewBox="0 0 42 30" aria-hidden="true">
        <rect x="1.5" y="1.5" width="39" height="27" fill="none" stroke="#111" stroke-width="3"/>
        <path d="M2 2 L21 17 L40 2 M2 28 L16 13 M40 28 L26 13" fill="none" stroke="#111" stroke-width="3"/>
      </svg>
      Tamsin@TamsinHarlowe.com
    </p>

    <p class="contact contact--web">
      <svg class="contact__icon" width="28" height="28" viewBox="0 0 30 30" aria-hidden="true">
        <circle cx="5" cy="25" r="4" fill="#111"/>
        <path d="M2 13 A15 15 0 0 1 17 28" fill="none" stroke="#111" stroke-width="4"/>
        <path d="M2 3 A25 25 0 0 1 27 28" fill="none" stroke="#111" stroke-width="4"/>
      </svg>
      www.tamsinharlowe.com
    </p>
  </section>
</main>
</body>
</html>
```